Business Card for Willowcrest Terrain Advisors

We need a business card for Willowcrest Terrain Advisors. The company website address is provided below. The company logo is attached. We provide specialized permafrost services to the mining, transportation, and oil & gas industries. The card should be prepared for:
Dominic Halloway, PhD.
Willowcrest Terrain Advisors
PO Box 418529
Birch Hollow, Alaska 99612
Direct: +1-907-555-2964
Email: dhalloway@terrainadvisors-example.com
Website: www.willowcrestterrainadvisors-example.com

```html
<!DOCTYPE html>
<html lang="en">
<head>
<meta charset="utf-8">
<title>Willowcrest Terrain Advisors — Business Card</title>
<link href="https://fonts.googleapis.com/css2?family=Open+Sans:wght@400;600&display=swap" rel="stylesheet">
<style>
  :root {
    --backdrop: #232323;
    --card-red: #b3161f;
    --card-red-deep: #8e0f17;
    --card-black: #141414;
    --ink-white: #f4f4f4;
    --ink-grey: #b9b9b9;
    --accent-red: #d4202a;
    --rule: #5a5a5a;
  }
  * { box-sizing: border-box; margin: 0; padding: 0; }
  html, body { width: 1200px; height: 1043px; overflow: hidden; }
  body {
    background: var(--backdrop);
    font-family: "Open Sans", Arial, sans-serif;
    display: flex;
    align-items: center;
    justify-content: center;
    gap: 60px;
  }
  .card {
    width: 525px;
    height: 300px;
    position: relative;
    overflow: hidden;
    box-shadow: 0 14px 30px rgba(0,0,0,.45);
  }

  /* Front */
  .card--front {
    background: linear-gradient(160deg, var(--card-red) 0%, var(--card-red-deep) 100%);
  }
  .front__backdrop-name {
    position: absolute;
    left: -20px;
    top: 40px;
    font-size: 118px;
    font-weight: 600;
    letter-spacing: 4px;
    color: rgba(0,0,0,.12);
    white-space: nowrap;
    text-transform: uppercase;
  }
  .front__wordmark {
    position: absolute;
    right: 46px;
    bottom: 70px;
    text-align: center;
    color: var(--ink-white);
    font-weight: 600;
    text-transform: uppercase;
  }
  .front__wordmark .line-main { font-size: 30px; letter-spacing: 4px; display: block; }
  .front__wordmark .line-sub { font-size: 11px; letter-spacing: 4.2px; display: block; margin-top: 2px; }

  /* Back */
  .card--back { background: var(--card-black); color: var(--ink-white); }
  .back__wordmark {
    position: absolute;
    left: 26px;
    top: 116px;
    width: 160px;
    text-align: center;
    font-weight: 600;
    text-transform: uppercase;
    color: var(--ink-white);
  }
  .back__wordmark .line-main { font-size: 19px; letter-spacing: 2px; display: block; }
  .back__wordmark .line-sub { font-size: 7.5px; letter-spacing: 2.6px; display: block; margin-top: 2px; }
  .back__divider {
    position: absolute;
    left: 205px;
    top: 40px;
    width: 1px;
    height: 172px;
    background: var(--rule);
  }
  .contact {
    position: absolute;
    left: 228px;
    top: 44px;
    right: 18px;
  }
  .contact__name { font-size: 17px; font-weight: 400; letter-spacing: .3px; }
  .contact__company { font-size: 10.5px; color: var(--ink-grey); margin-top: 2px; }
  .contact__list { list-style: none; margin-top: 16px; }
  .contact__list li {
    display: flex;
    align-items: center;
    gap: 10px;
    font-size: 10px;
    color: var(--ink-grey);
    margin-bottom: 11px;
    white-space: nowrap;
  }
  .contact__list svg { width: 12px; height: 12px; flex: none; fill: var(--accent-red); }
  .back__address {
    position: absolute;
    left: 228px;
    bottom: 40px;
    font-size: 12.5px;
    color: var(--ink-white);
    letter-spacing: .2px;
  }
</style>
</head>
<body>
  <section class="card card--front" aria-label="Business card front">
    <div class="front__backdrop-name" aria-hidden="true">Willowcrest</div>
    <div class="front__wordmark">
      <span class="line-main">Willowcrest</span>
      <span class="line-sub">Terrain Advisors</span>
    </div>
  </section>

  <section class="card card--back" aria-label="Business card back">
    <div class="back__wordmark">
      <span class="line-main">Willowcrest</span>
      <span class="line-sub">Terrain Advisors</span>
    </div>
    <div class="back__divider"></div>
    <div class="contact">
      <p class="contact__name">Dominic Halloway, PhD.</p>
      <p class="contact__company">Willowcrest Terrain Advisors</p>
      <ul class="contact__list">
        <li>
          <svg viewBox="0 0 24 24" aria-hidden="true"><path d="M6.6 10.8a15.1 15.1 0 0 0 6.6 6.6l2.2-2.2c.3-.3.7-.4 1-.2 1.1.4 2.3.6 3.6.6.6 0 1 .4 1 1V20c0 .6-.4 1-1 1A17 17 0 0 1 3 4c0-.6.4-1 1-1h3.5c.6 0 1 .4 1 1 0 1.3.2 2.5.6 3.6.1.3 0 .7-.2 1z"/></svg>
          +1-907-555-2964
        </li>
        <li>
          <svg viewBox="0 0 24 24" aria-hidden="true"><path d="M2 5h20v14H2zm2 2v.5l8 5 8-5V7z"/></svg>
          dhalloway@terrainadvisors-example.com
        </li>
        <li>
          <svg viewBox="0 0 24 24" aria-hidden="true"><circle cx="12" cy="12" r="10"/></svg>
          www.willowcrestterrainadvisors-example.com
        </li>
      </ul>
    </div>
    <p class="back__address">PO Box 418529 Birch Hollow, Alaska 99612</p>
  </section>
</body>
</html>
```